Design for online reviews widget

Attached is a wireframe of a widget we need designing to display reviews on websites from multiple sources. We need this provided at 3 different sizes including full screen, contained (like the wireframe) and mobile.
You have completely free rein on the styling.
The only elements that should remain untouched are the blue stars (https://www.filquarry.net/s/8vtmwp2291zq4h/kv%20stars.ai?dl=0) and powered by logo at the bottom.
Ignore the menu at the top of the wireframe, this is just from the website the widget will be placed on.
Businesses

```html
<!DOCTYPE html>
<html lang="en">
<head>
<meta charset="utf-8">
<title>Reviews Widget – Website and Mobile Layouts</title>
<link rel="stylesheet" href="https://fonts.googleapis.com/css2?family=Roboto:wght@400;500;700&family=Roboto+Condensed:wght@400&display=swap">
<style>
:root{
  --page:#ffffff;
  --nav:#232323;
  --nav-text:#ffffff;
  --accent:#5ba71b;
  --band:#f2f2f2;
  --card:#ffffff;
  --ink:#111111;
  --muted:#9a9a9a;
  --badge:#2aa8e6;
  --badge-edge:#8fd2f3;
  --gold:#e6bd00;
  --arrow:#e3e3e3;
}
*{box-sizing:border-box;margin:0;padding:0}
html,body{width:1200px;height:821px;overflow:hidden;background:var(--page)}
body{position:relative;font-family:"Roboto",Arial,sans-serif;color:var(--ink)}
svg.defs{position:absolute;width:0;height:0}

/* ---------- website layout ---------- */
.site{position:absolute;left:57px;top:123px;width:754px;height:513px;background:var(--page);
  box-shadow:0 12px 30px rgba(0,0,0,.12)}
.site-nav{height:31px;background:var(--nav);display:flex;align-items:stretch;padding-left:31px;
  font-family:"Roboto Condensed","Arial Narrow",sans-serif}
.site-nav a{color:var(--nav-text);text-decoration:none;font-size:9.6px;display:flex;align-items:center;
  padding:0 11px;white-space:nowrap}
.site-nav a.active{background:var(--accent)}
.site-nav .caret{display:inline-block;width:0;height:0;border-left:3.5px solid transparent;
  border-right:3.5px solid transparent;border-top:6px solid var(--nav-text);margin-left:3px}

.score-badges{position:absolute;left:0;right:0;display:flex;justify-content:center}
.score-badges svg{display:block}
.site .score-badges{top:62px;gap:6px}
.site .score-badges svg{width:29px;height:29px}
.score-title{position:absolute;left:0;right:0;text-align:center;font-weight:700}
.site .score-title{top:105px;font-size:17px;letter-spacing:.1px}

.review-band{position:absolute;left:42px;top:154px;width:670px;height:261px;background:var(--band)}
.review-band .carousel-arrow{position:absolute;top:129px;width:14px;height:14px;border-radius:50%;
  background:var(--arrow);display:flex;align-items:center;justify-content:center}
.review-band .carousel-arrow.prev{left:13px}
.review-band .carousel-arrow.next{left:642px}

.review-card{position:absolute;background:var(--card)}
.site .review-card{top:28px;width:193px;height:208px}
.quote-mark{position:absolute;display:block}
.site .quote-mark{left:14px;top:17px;width:18px;height:14px}
.review-title{position:absolute;font-weight:700;line-height:1.2}
.site .review-title{left:40px;top:15px;width:124px;font-size:8.5px}
.review-body{position:absolute;color:var(--muted)}
.site .review-body{left:14px;top:47px;width:172px;font-size:6.9px;line-height:8.85px}
.review-meta{position:absolute;color:var(--accent);line-height:1.1}
.site .review-meta{left:14px;top:148px;font-size:7.4px}
.source-name{position:absolute;font-weight:500;color:var(--ink)}
.site .source-name{left:14px;top:174px;font-size:11px}
.rating{position:absolute;display:flex;gap:1px}
.site .rating{left:14px;top:193px}
.site .rating svg{width:8.5px;height:8.5px}

.powered{position:absolute;display:flex;align-items:center}
.powered .dot{border-radius:50%;background:var(--badge)}
.powered .label{display:flex;flex-direction:column;line-height:1}
.site .powered{left:572px;top:439px;gap:6px}
.site .powered .dot{width:26px;height:26px}
.site .powered small{font-size:10.5px;font-weight:500}
.site .powered strong{font-size:17px;font-weight:700;margin-top:2px}

/* ---------- mobile layout ---------- */
.mobile{position:absolute;left:887px;top:49px;width:262px;height:604px;background:#f6f6f6;
  box-shadow:0 12px 30px rgba(0,0,0,.12)}
.mobile .score-badges{top:18px;gap:2px}
.mobile .score-badges svg{width:11px;height:11px}
.mobile .score-title{top:35px;font-size:6px}
.mobile .review-card{left:4px;width:255px}
.mobile .quote-mark{left:11px;top:10px;width:14px;height:11px}
.mobile .review-title{left:33px;top:8px;width:134px;font-size:6.3px}
.mobile .review-body{left:12px;top:34px;width:228px;font-size:5.5px;line-height:7.45px}
.mobile .review-meta{left:12px;font-size:5.6px}
.mobile .source-name{left:12px;font-size:9px}
.mobile .rating{left:12px}
.mobile .rating svg{width:6.3px;height:6.3px}
.mobile .powered{left:133px;top:577px;transform:translateX(-50%);gap:3px}
.mobile .powered .dot{width:12px;height:12px}
.mobile .powered small{font-size:4px}
.mobile .powered strong{font-size:7px;font-weight:700;margin-top:1px}

.layout-label{position:absolute;top:697px;font-size:25px;font-weight:400;letter-spacing:.4px;
  transform:translateX(-50%);white-space:nowrap}
</style>
</head>
<body>

<svg class="defs" aria-hidden="true">
  <defs>
    <symbol id="score-badge" viewBox="0 0 40 40">
      <circle cx="20" cy="20" r="19" fill="var(--badge)"/>
      <circle cx="20" cy="20" r="16.5" fill="none" stroke="var(--badge-edge)" stroke-width="1.2"/>
      <polygon fill="#fff" points="20,8 23.3,16.2 32,16.6 25.2,22 27.5,30.5 20,25.6 12.5,30.5 14.8,22 8,16.6 16.7,16.2"/>
    </symbol>
    <symbol id="star-full" viewBox="0 0 20 20">
      <polygon fill="var(--gold)" points="10,1 12.6,7.2 19.3,7.6 14.1,11.9 15.8,18.5 10,14.8 4.2,18.5 5.9,11.9 0.7,7.6 7.4,7.2"/>
    </symbol>
    <symbol id="star-empty" viewBox="0 0 20 20">
      <polygon fill="none" stroke="var(--gold)" stroke-width="1.8" points="10,2.5 12.1,7.9 17.8,8.3 13.4,11.9 14.8,17.5 10,14.4 5.2,17.5 6.6,11.9 2.2,8.3 7.9,7.9"/>
    </symbol>
    <symbol id="quote" viewBox="0 0 26 20">
      <path fill="var(--accent)" d="M1 20V11C1 5 4 1.5 10 0.5L11 3C8 4 6.5 6 6.5 9H11V20ZM15 20V11C15 5 18 1.5 24 0.5L25 3C22 4 20.5 6 20.5 9H25V20Z"/>
    </symbol>
    <symbol id="chev-left" viewBox="0 0 10 10"><path d="M6.5 2 3.5 5l3 3" fill="none" stroke="#fff" stroke-width="1.4"/></symbol>
    <symbol id="chev-right" viewBox="0 0 10 10"><path d="M3.5 2l3 3-3 3" fill="none" stroke="#fff" stroke-width="1.4"/></symbol>
  </defs>
</svg>

<!-- Website layout -->
<section class="site">
  <nav class="site-nav">
    <a href="#">HOME</a>
    <a href="#">ABOUT<span class="caret"></span></a>
    <a href="#">WINDOWS<span class="caret"></span></a>
    <a href="#">DOORS<span class="caret"></span></a>
    <a href="#">ORANGERIES &amp; EXTENSIONS<span class="caret"></span></a>
    <a href="#">ROOFS<span class="caret"></span></a>
    <a href="#">OUR WORK<span class="caret"></span></a>
    <a href="#" class="active">REVIEWS<span class="caret"></span></a>
    <a href="#">BLOG</a>
    <a href="#">CONTACT</a>
  </nav>

  <div class="score-badges">
    <svg><use href="#score-badge"/></svg><svg><use href="#score-badge"/></svg><svg><use href="#score-badge"/></svg><svg><use href="#score-badge"/></svg><svg><use href="#score-badge"/></svg>
  </div>
  <h1 class="score-title">Combined Review Score 4.3 out of 5</h1>

  <div class="review-band">
    <span class="carousel-arrow prev"><svg width="9" height="9"><use href="#chev-left"/></svg></span>
    <span class="carousel-arrow next"><svg width="9" height="9"><use href="#chev-right"/></svg></span>

    <article class="review-card" style="left:37px">
      <svg class="quote-mark"><use href="#quote"/></svg>
      <h2 class="review-title">Front door with windows each side and side window</h2>
      <p class="review-body">This is the second time we have used sentinel home Improvments and the service is amazing! Owen came round several times as we kept changing our minds and he was so helpful and gave us good advice, and the guys who do the fitting are efficient and tidy. I've got to say the end result is amazing and I have recommended to many of friends. Thanks Sentinel Reliablity: 9.38 Courtesy: 10 Tidiness: 9.84 Workmanship: 10</p>
      <p class="review-meta">Verified 28th September 2021<br>Located in Harlow</p>
      <span class="source-name">TradeVouch</span>
      <div class="rating"><svg><use href="#star-full"/></svg><svg><use href="#star-full"/></svg><svg><use href="#star-full"/></svg><svg><use href="#star-empty"/></svg><svg><use href="#star-empty"/></svg></div>
    </article>

    <article class="review-card" style="left:238px">
      <svg class="quote-mark"><use href="#quote"/></svg>
      <h2 class="review-title" style="width:112px">Positive: Professionalism, Quality, Value</h2>
      <p class="review-body">The team did a good job of replacing a large feature window spanning two floors, as well as the others in my property. They're a professional group who were willing to work out solutions to any problem, especially compared to other companies. Prices are fair, and my new UPVC windows look great. Special thanks to Ray for being so accommodating and for the good communication throughout.<br>Service: Window installation</p>
      <p class="review-meta">11 months ago<br>&nbsp;by Henry Dale</p>
      <span class="source-name">Searchly</span>
      <div class="rating"><svg><use href="#star-full"/></svg><svg><use href="#star-full"/></svg><svg><use href="#star-full"/></svg><svg><use href="#star-empty"/></svg><svg><use href="#star-empty"/></svg></div>
    </article>

    <article class="review-card" style="left:440px">
      <svg class="quote-mark"><use href="#quote"/></svg>
      <h2 class="review-title" style="width:130px">Brilliant all round professional, friendly service.</h2>
      <p class="review-body">This home run friendly business was a real pleasure to deal with. From the professional, no pressure quote, nothing was too much trouble to ensure everything is as required for your needs with the quote and fitting. The workmanship and double glazing being fitted was brilliant and my home/outdoors was left tidy and clean leaving an outstanding impression for such an all round professional job. I would not hesitate to recommend this company, such a brilliant service from great hardworking people that care about their service.</p>
      <p class="review-meta">Verified 28th September 2021<br>Located in Harlow</p>
      <span class="source-name">Dialbook</span>
      <div class="rating"><svg><use href="#star-full"/></svg><svg><use href="#star-full"/></svg><svg><use href="#star-full"/></svg><svg><use href="#star-empty"/></svg><svg><use href="#star-empty"/></svg></div>
    </article>
  </div>

  <div class="powered">
    <span class="dot"></span>
    <span class="label"><small>Powered by</small><strong>ScoreGather</strong></span>
  </div>
</section>

<!-- Mobile layout -->
<section class="mobile">
  <div class="score-badges">
    <svg><use href="#score-badge"/></svg><svg><use href="#score-badge"/></svg><svg><use href="#score-badge"/></svg><svg><use href="#score-badge"/></svg><svg><use href="#score-badge"/></svg>
  </div>
  <h1 class="score-title">Combined Review Score 4.3 out of 5</h1>

  <article class="review-card" style="top:50px;height:141px">
    <svg class="quote-mark"><use href="#quote"/></svg>
    <h2 class="review-title">Front door with windows each side and side window</h2>
    <p class="review-body">This is the second time we have used sentinel home Improvments and the service is amazing! Owen came round several times as we keep changing our minds and he was so helpful and gave us good advice, and the guys who do the fitting are efficient and tidy. I've got to say the end result is amazing and I have recommended to many of friends. Thanks Sentinel Reliablity: 9.38 Courtesy: 10 Tidiness: 9.84 Workmanship: 10</p>
    <p class="review-meta" style="top:91px">Verified 28th September 2021 Located in Harlow</p>
    <span class="source-name" style="top:101px">TradeVouch</span>
    <div class="rating" style="top:118px"><svg><use href="#star-full"/></svg><svg><use href="#star-full"/></svg><svg><use href="#star-full"/></svg><svg><use href="#star-empty"/></svg><svg><use href="#star-empty"/></svg></div>
  </article>

  <article class="review-card" style="top:196px;height:176px">
    <svg class="quote-mark"><use href="#quote"/></svg>
    <h2 class="review-title">Positive: Professionalism, Quality, Value</h2>
    <p class="review-body">The team did a good job of replacing a large feature window spanning two floors, as well as the others in my property. They're a professional group who were willing to work out solutions to any problem, especially compared to other companies. Prices are fair, and my new UPVC windows look great. Special thanks to Ray for being so accommodating and for the good communication throughout.<br>Service: Window installation</p>
    <p class="review-meta" style="top:92px;left:9px">11 months ago by Henry Dale</p>
    <span class="source-name" style="top:103px;left:9px">Searchly</span>
    <div class="rating" style="top:121px;left:9px"><svg><use href="#star-full"/></svg><svg><use href="#star-full"/></svg><svg><use href="#star-full"/></svg><svg><use href="#star-empty"/></svg><svg><use href="#star-empty"/></svg></div>
  </article>

  <article class="review-card" style="top:381px;height:177px">
    <svg class="quote-mark"><use href="#quote"/></svg>
    <h2 class="review-title">Brilliant all round professional, friendly service.</h2>
    <p class="review-body">This home run friendly business was a real pleasure to deal with. From the professional, no pressure quote, nothing was too much trouble to ensure everything is as required for your needs with the quote and fitting. The workmanship and double glazing being fitted was brilliant and my home/outdoors was left tidy and clean leaving an outstanding impression for such an all round professional job. I would not hesitate to recommend this company, such a brilliant service from great hardworking people that care about their service.</p>
    <p class="review-meta" style="top:101px">Verified 28th September 2021 Located in Harlow</p>
    <span class="source-name" style="top:113px">Dialbook</span>
    <div class="rating" style="top:132px"><svg><use href="#star-full"/></svg><svg><use href="#star-full"/></svg><svg><use href="#star-full"/></svg><svg><use href="#star-empty"/></svg><svg><use href="#star-empty"/></svg></div>
  </article>

  <div class="powered">
    <span class="dot"></span>
    <span class="label"><small>Powered by</small><strong>ScoreGather</strong></span>
  </div>
</section>

<p class="layout-label" style="left:442px">Website Layout</p>
<p class="layout-label" style="left:1017px">Mobile Layout</p>

</body>
</html>
```